User-interface and web design for new forum-style communication platform

We developed a new forum-style communication platform specially targetting stock investors to share and discuss information on companies listed on the stock exchange.

You have complete freedom for designing the user-interface and web design. Designs should include all features listed below.

Please read the attached document for full specifications. Also attached is a mockup of the layout, but this is only directional. A mockup for the user-profile is also attached, but does not need to be designed.

This project focusses on the homepage and thread view.

The winner(s) will be asked to design the complete project. (create thread box, user profile, registering, settings...)

We are looking for a well thought out, smart design that incorporates the specifications in the attached document. Please do not hesitate to contact us if anything is not clear.

Target Market(s)

Stock investors from 25 to 60 years old (the people that are currently on investor forums)

Industry/Entity Type

Communication

Font styles to use
Sans Serif

Colors

Designer to choose colors to be used in the design.

Requirements
Must have
• Full homepage design & Thread view specified in the attached document.
Nice to have
• Create thread view
- Field for adding tags
- field for subject of the thread
- text box with basic text editing
- method for sharing media
Should not have
• Logo design.

```html
<!DOCTYPE html>
<html lang="en">
<head>
<meta charset="utf-8">
<title>Forum – Thread list</title>
<link rel="stylesheet" href="https://fonts.googleapis.com/css2?family=Arimo:wght@400;700&family=Ubuntu:wght@400;500;700&family=Oswald:wght@400;500&display=swap">
<style>
  :root {
    --page-bg: #f1f1f1;
    --white: #ffffff;
    --dark: #2d2d2d;
    --orange: #f68b0c;
    --orange-text: #e36c09;
    --heading-red: #8a1c00;
    --link-blue: #1a6fd1;
    --grey-line: #cfcfcf;
    --grey-soft: #ededed;
    --grey-btn: #6b6b6b;
    --text: #333333;
    --muted: #999999;
  }
  * { box-sizing: border-box; margin: 0; padding: 0; }
  html, body { width: 1200px; height: 1106px; overflow: hidden; }
  body {
    position: relative;
    background: var(--page-bg);
    font-family: "Arimo", Arial, sans-serif;
    color: var(--text);
    font-size: 11.5px;
  }
  .abs { position: absolute; }

  /* Top bar */
  .topbar { left: 126px; top: 22px; width: 949px; height: 34px; background: #fafafa; border-top: 3px solid var(--orange); }
  .topbar-search { position: absolute; left: 342px; top: 0; width: 463px; height: 31px; background: var(--white); border-left: 1px solid #e6e6e6; color: var(--muted); font-family: "Ubuntu", sans-serif; font-size: 12px; line-height: 31px; padding-left: 14px; }
  .topbar-go { position: absolute; left: 805px; top: 0; width: 35px; height: 31px; background: var(--orange); display: flex; align-items: center; justify-content: center; }
  .topbar-go::before { content: ""; position: absolute; left: -6px; top: 10px; border: 6px solid transparent; border-right-color: var(--orange); border-left: 0; }
  .topbar-btn { position: absolute; top: 0; height: 31px; background: var(--grey-btn); color: var(--white); font-family: "Ubuntu", sans-serif; font-size: 13px; line-height: 31px; text-align: center; }
  .btn-save { left: 840px; width: 49px; }
  .btn-clear { left: 891px; width: 58px; }

  /* Header */
  .header { left: 126px; top: 56px; width: 949px; height: 86px; background: var(--white); }
  .company { position: absolute; left: 32px; top: 12px; width: 160px; text-align: center; font-family: "Ubuntu", sans-serif; font-weight: 500; font-size: 25px; line-height: 27px; color: var(--dark); }
  .banner { position: absolute; left: 520px; top: 24px; width: 200px; text-align: center; font-family: "Ubuntu", sans-serif; font-weight: 700; font-size: 28px; color: #e8e8e8; }

  /* Nav */
  .nav { left: 126px; top: 142px; width: 949px; height: 44px; background: var(--dark); border-bottom: 4px solid var(--orange); }
  .nav-item { position: absolute; top: 0; height: 40px; line-height: 40px; color: var(--white); font-family: "Ubuntu", sans-serif; font-size: 13px; }
  .nav-sep { position: absolute; top: 4px; width: 1px; height: 32px; background: #4a4a4a; border-right: 1px solid #1d1d1d; }
  .user-select { position: absolute; left: 877px; top: 11px; width: 60px; height: 20px; background: var(--white); border: 1px solid #bbb; font-family: "Ubuntu", sans-serif; font-size: 12px; line-height: 18px; padding-left: 7px; color: #222; }
  .user-select::after { content: ""; position: absolute; right: 7px; top: 7px; border: 5px solid transparent; border-top: 6px solid #222; border-bottom: 0; }

  /* Main panel */
  .main { left: 126px; top: 212px; width: 949px; height: 827px; background: var(--white); }

  .breadcrumb { left: 146px; top: 231px; font-size: 12px; color: #555; }
  .breadcrumb a { color: var(--link-blue); text-decoration: none; }
  .breadcrumb .sep { color: var(--link-blue); margin: 0 5px; font-size: 11px; }

  .tabs { left: 144px; top: 257px; width: 220px; height: 28px; background: var(--orange); border: 1px solid #e07b00; display: flex; font-family: "Ubuntu", sans-serif; font-size: 13px; }
  .tab { line-height: 26px; color: var(--white); padding: 0 12px; }
  .tab.active { background: var(--dark); }
  .create-thread { left: 643px; top: 259px; width: 109px; height: 26px; background: var(--dark); color: var(--white); border-radius: 3px; font-family: "Ubuntu", sans-serif; font-weight: 500; font-size: 12.5px; line-height: 26px; text-align: center; }

  /* Posts */
  .post { left: 145px; width: 609px; border: 3px solid #d6d6d6; background: var(--white); }
  .avatar-frame { position: absolute; left: 14px; top: 12px; width: 101px; height: 101px; border: 1px solid #e0e0e0; border-radius: 4px; padding: 3px; box-shadow: 0 1px 2px rgba(0,0,0,.12); background: var(--white); }
  .avatar-fill { width: 100%; height: 100%; border-radius: 3px; background: linear-gradient(135deg, #7d5a3c 0%, #c89a78 45%, #e9e4de 100%); }
  .post-body { position: absolute; left: 126px; top: 16px; width: 460px; }
  .post-title { font-weight: 700; font-size: 13.5px; color: var(--heading-red); line-height: 17px; }
  .post-meta { font-size: 12.5px; color: var(--orange-text); line-height: 16px; }
  .post-text { margin-top: 13px; font-size: 11px; line-height: 16.2px; color: #333; }
  .post-bar { position: absolute; left: 4px; right: 4px; bottom: 4px; height: 32px; background: var(--grey-soft); display: flex; align-items: center; padding-left: 15px; font-size: 12px; }
  .post-bar .read-more { color: var(--link-blue); text-decoration: underline; margin-right: 25px; }
  .post-bar .stat { color: #444; margin-right: 22px; }
  .actions { margin-left: auto; display: flex; gap: 8px; margin-right: 2px; }
  .action { height: 25px; background: var(--white); border: 1px solid #d2d2d2; border-radius: 3px; display: flex; align-items: center; gap: 4px; padding: 0 7px; font-weight: 700; font-size: 12.5px; color: #666; }

  .reply-row { left: 148px; width: 607px; height: 45px; }
  .reply-avatar { position: absolute; left: 0; top: 2px; width: 44px; height: 44px; border: 1px solid #e0e0e0; padding: 2px; border-radius: 3px; }
  .reply-input { position: absolute; left: 67px; top: 0; width: 540px; height: 45px; border: 3px solid #e3e3e3; border-radius: 6px; font-size: 11.5px; color: #333; padding: 8px 0 0 13px; }

  /* Sidebar */
  .stats { left: 781px; top: 225px; width: 281px; height: 85px; border: 2px solid #dcdcdc; display: flex; background: var(--white); }
  .stat-cell { flex: 1; border-right: 1px solid #dcdcdc; text-align: center; padding-top: 7px; font-family: "Oswald", sans-serif; color: #555; }
  .stat-cell:last-child { border-right: 0; }
  .stat-cell .num { font-size: 11px; margin-top: 2px; line-height: 14px; }
  .stat-cell .label { font-size: 12px; font-weight: 500; letter-spacing: .2px; line-height: 16px; }

  .side-title { left: 782px; width: 280px; display: flex; align-items: center; font-family: "Oswald", sans-serif; font-weight: 500; font-size: 16px; color: #333; letter-spacing: .4px; }
  .side-title::after { content: ""; flex: 1; height: 10px; margin-left: 10px; background: repeating-linear-gradient(135deg, #d8d8d8 0 2px, transparent 2px 4px); }

  .side-box { left: 782px; width: 280px; border: 1px solid #dcdcdc; border-bottom: 3px solid var(--orange); background: var(--white); }
  .users-search { position: absolute; left: 10px; top: 13px; width: 256px; height: 37px; background: #f2f2f2; border: 1px solid #dcdcdc; border-radius: 3px; font-size: 13px; color: #777; line-height: 35px; padding-left: 12px; }
  .users-btn { position: absolute; left: 10px; top: 58px; width: 84px; height: 27px; background: #a9a9a9; border: 1px solid #8c8c8c; border-radius: 4px; color: var(--white); font-family: "Oswald", sans-serif; font-size: 13.5px; line-height: 25px; text-align: center; }

  .list { position: absolute; left: 20px; top: 15px; list-style: none; font-size: 12px; color: #333; }
  .list li { line-height: 21.6px; }
  .list li::before { content: "» "; }
  .show-all { position: absolute; left: 3px; right: 3px; bottom: 3px; height: 26px; background: #efefef; text-align: right; padding-right: 12px; font-weight: 700; font-size: 12px; line-height: 26px; color: #333; }
  .show-all span { text-decoration: underline; }

  .footer { left: 125px; top: 1058px; width: 950px; height: 39px; background: var(--dark); color: var(--white); font-family: "Ubuntu", sans-serif; font-size: 11.5px; text-align: center; line-height: 39px; }
</style>
</head>
<body>

<div class="abs topbar">
  <div class="topbar-search">SEARCH :</div>
  <div class="topbar-go">
    <svg width="20" height="20" viewBox="0 0 20 20"><circle cx="8" cy="8" r="5.5" fill="none" stroke="#fff" stroke-width="2.2"/><path d="M12 12l6 6" stroke="#fff" stroke-width="3" stroke-linecap="round"/></svg>
  </div>
  <div class="topbar-btn btn-save">SAVE</div>
  <div class="topbar-btn btn-clear">CLEAR</div>
</div>

<header class="abs header">
  <div class="company">COMAPNY<br>NAME</div>
  <div class="banner">BANNER</div>
</header>

<nav class="abs nav">
  <span class="nav-item" style="left:31px">HOME</span>
  <span class="nav-sep" style="left:89px"></span>
  <span class="nav-item" style="left:114px">SETTING</span>
  <span class="nav-sep" style="left:188px"></span>
  <span class="nav-item" style="left:213px">MANAGE</span>
  <div class="user-select">User</div>
</nav>

<main class="abs main"></main>

<div class="abs breadcrumb">
  <a href="#">Home</a><span class="sep">&gt;</span><a href="#">Conversations</a><span class="sep">&gt;</span><a href="#">Public</a><span class="sep">&gt;</span>Northwind Ledger
</div>

<div class="abs tabs">
  <span class="tab active">Public</span><span class="tab">Following</span><span class="tab">Contacts</span>
</div>
<div class="abs create-thread">CREATE THREAD</div>

<!-- Thread 1 -->
<article class="abs post" style="top:295px;height:186px">
  <div class="avatar-frame"><div class="avatar-fill" role="img" aria-label="Author profile photo"></div></div>
  <div class="post-body">
    <h2 class="post-title">Heading title</h2>
    <p class="post-meta">Posted by Arun Mehta on &nbsp;04/27/2014</p>
    <p class="post-text">Lorem Ipsum is simply dummy text of the printing and typesetting industry. Lorem Ipsum has been the industry's standard dummy text ever since the 1500s, when an unknown printer took a galley of type and scrambled it to make a type specimen book. It has survived not only five centuries, but also the leap into electronic typesetting,</p>
  </div>
  <div class="post-bar">
    <span class="read-more">Read more</span><span class="stat">23 reply</span><span class="stat">250 View</span>
    <div class="actions">
      <span class="action"><svg width="14" height="14" viewBox="0 0 14 14"><circle cx="7" cy="7" r="6.5" fill="#3fae49"/><path d="M4 7a3 3 0 1 0 3-3" fill="none" stroke="#fff" stroke-width="1.5"/><path d="M7 2v4l-2-2z" fill="#fff"/></svg>Reply</span>
      <span class="action"><svg width="15" height="15" viewBox="0 0 15 15"><circle cx="6" cy="9" r="4" fill="none" stroke="#2a8bd6" stroke-width="1.8"/><path d="M9 6l4-4M9.5 2h3.5v3.5" fill="none" stroke="#2a8bd6" stroke-width="1.8"/></svg>Share</span>
      <span class="action"><svg width="11" height="11" viewBox="0 0 11 11"><circle cx="5.5" cy="5.5" r="3.5" fill="#e8431d"/><circle cx="5.5" cy="5.5" r="5" fill="none" stroke="#f28a6d" stroke-dasharray="1.5 1.3"/></svg>Favourite</span>
    </div>
  </div>
</article>
<div class="abs reply-row" style="top:498px">
  <div class="reply-avatar"><div class="avatar-fill" role="img" aria-label="Current user profile photo"></div></div>
  <div class="reply-input">Type your reply here</div>
</div>

<!-- Thread 2 -->
<article class="abs post" style="top:562px;height:169px">
  <div class="avatar-frame"><div class="avatar-fill" role="img" aria-label="Author profile photo"></div></div>
  <div class="post-body">
    <h2 class="post-title">Heading title</h2>
    <p class="post-meta">Posted by Arun Mehta on &nbsp;04/27/2014</p>
    <p class="post-text">Lorem Ipsum is simply dummy text of the printing and typesetting industry. Lorem Ipsum has been the industry's standard dummy text ever since the 1500s, when an unknown printer took a galley of type and scrambled it to make a type specimen book. It has survived not only five</p>
  </div>
  <div class="post-bar">
    <span class="read-more">Read more</span><span class="stat">23 reply</span><span class="stat">250 View</span>
    <div class="actions">
      <span class="action"><svg width="14" height="14" viewBox="0 0 14 14"><circle cx="7" cy="7" r="6.5" fill="#3fae49"/><path d="M4 7a3 3 0 1 0 3-3" fill="none" stroke="#fff" stroke-width="1.5"/><path d="M7 2v4l-2-2z" fill="#fff"/></svg>Reply</span>
      <span class="action"><svg width="15" height="15" viewBox="0 0 15 15"><circle cx="6" cy="9" r="4" fill="none" stroke="#2a8bd6" stroke-width="1.8"/><path d="M9 6l4-4M9.5 2h3.5v3.5" fill="none" stroke="#2a8bd6" stroke-width="1.8"/></svg>Share</span>
      <span class="action"><svg width="11" height="11" viewBox="0 0 11 11"><circle cx="5.5" cy="5.5" r="3.5" fill="#e8431d"/><circle cx="5.5" cy="5.5" r="5" fill="none" stroke="#f28a6d" stroke-dasharray="1.5 1.3"/></svg>Favourite</span>
    </div>
  </div>
</article>
<div class="abs reply-row" style="top:738px">
  <div class="reply-avatar"><div class="avatar-fill" role="img" aria-label="Current user profile photo"></div></div>
  <div class="reply-input">Type your reply here</div>
</div>

<!-- Thread 3 -->
<article class="abs post" style="top:811px;height:159px">
  <div class="avatar-frame"><div class="avatar-fill" role="img" aria-label="Author profile photo"></div></div>
  <div class="post-body">
    <h2 class="post-title">Heading title</h2>
    <p class="post-meta">Posted by Arun Mehta on &nbsp;04/27/2014</p>
    <p class="post-text">Lorem Ipsum is simply dummy text of the printing and typesetting industry. Lorem Ipsum has been the industry's standard dummy text ever since the 1500s, when an unknown printer took</p>
  </div>
  <div class="post-bar">
    <span class="read-more">Read more</span><span class="stat">23 reply</span><span class="stat">250 View</span>
    <div class="actions">
      <span class="action"><svg width="14" height="14" viewBox="0 0 14 14"><circle cx="7" cy="7" r="6.5" fill="#3fae49"/><path d="M4 7a3 3 0 1 0 3-3" fill="none" stroke="#fff" stroke-width="1.5"/><path d="M7 2v4l-2-2z" fill="#fff"/></svg>Reply</span>
      <span class="action"><svg width="15" height="15" viewBox="0 0 15 15"><circle cx="6" cy="9" r="4" fill="none" stroke="#2a8bd6" stroke-width="1.8"/><path d="M9 6l4-4M9.5 2h3.5v3.5" fill="none" stroke="#2a8bd6" stroke-width="1.8"/></svg>Share</span>
      <span class="action"><svg width="11" height="11" viewBox="0 0 11 11"><circle cx="5.5" cy="5.5" r="3.5" fill="#e8431d"/><circle cx="5.5" cy="5.5" r="5" fill="none" stroke="#f28a6d" stroke-dasharray="1.5 1.3"/></svg>Favourite</span>
    </div>
  </div>
</article>
<div class="abs reply-row" style="top:979px">
  <div class="reply-avatar"><div class="avatar-fill" role="img" aria-label="Current user profile photo"></div></div>
  <div class="reply-input">Type your reply here</div>
</div>

<!-- Sidebar -->
<aside class="abs stats">
  <div class="stat-cell">
    <svg width="36" height="30" viewBox="0 0 36 30"><circle cx="12" cy="8" r="6" fill="#333"/><path d="M1 28c0-8 5-12 11-12s11 4 11 12z" fill="#333"/><circle cx="23" cy="8" r="6" fill="#333"/><path d="M14 28c0-8 4-12 9-12s12 4 12 12z" fill="#333"/></svg>
    <div class="num">20</div><div class="label">NEW FOLLOWER</div>
  </div>
  <div class="stat-cell">
    <svg width="30" height="32" viewBox="0 0 30 32"><rect x="5" y="1" width="22" height="30" rx="2" fill="#333"/><rect x="3" y="6" width="5" height="3" fill="#333" stroke="#fff" stroke-width="1"/><rect x="3" y="14" width="5" height="3" fill="#333" stroke="#fff" stroke-width="1"/><rect x="3" y="22" width="5" height="3" fill="#333" stroke="#fff" stroke-width="1"/><circle cx="17" cy="12" r="4" fill="#fff"/><path d="M10 24c0-5 3-7 7-7s7 2 7 7z" fill="#fff"/></svg>
    <div class="num">40</div><div class="label">CONTACTS LIST</div>
  </div>
  <div class="stat-cell">
    <svg width="30" height="32" viewBox="0 0 30 32"><circle cx="15" cy="8" r="6.5" fill="#333"/><path d="M3 31c0-10 5-15 12-15s12 5 12 15z" fill="#333"/><path d="M11 16l4 5 4-5z" fill="#fff"/><path d="M14 20h2l1 8-2 2-2-2z" fill="#fff"/></svg>
    <div class="num">40</div><div class="label">VIEW PROFILE</div>
  </div>
</aside>

<h3 class="abs side-title" style="top:327px">USERS</h3>
<section class="abs side-box" style="top:359px;height:98px">
  <div class="users-search">SEARCH :</div>
  <div class="users-btn">SEARCH</div>
</section>

<h3 class="abs side-title" style="top:481px">SAVED FILTER</h3>
<section class="abs side-box" style="top:513px;height:134px">
  <ul class="list"><li>Item one</li><li>Item one</li><li>Item one</li><li>Item one</li></ul>
  <div class="show-all"><span>Show All</span></div>
</section>

<h3 class="abs side-title" style="top:663px">POPULAR TAGS</h3>
<section class="abs side-box" style="top:695px;height:134px">
  <ul class="list"><li>Item one</li><li>Item one</li><li>Item one</li><li>Item one</li></ul>
  <div class="show-all"><span>Show All</span></div>
</section>

<h3 class="abs side-title" style="top:848px">POPULAR CONTRIBUTORS</h3>
<section class="abs side-box" style="top:880px;height:134px">
  <ul class="list"><li>Item one</li><li>Item one</li><li>Item one</li><li>Item one</li></ul>
  <div class="show-all"><span>Show All</span></div>
</section>

<footer class="abs footer">Copyright 2014. All Rights Reserved</footer>

</body>
</html>
```